Laser, Vireln, fillers,

I need a few designs for Vireln, dermal fillers, laser IPL, Hair removal, hyperpigmentation removal, scar reduction resurface, PRP Hair restoration and PRP joint injections. Office number for appointments is 555-210-4836

Requirements
Must have
• Use the pictures below for dermal fillers need to show how dermal fillers improve

```html
<!DOCTYPE html>
<html lang="en">
<head>
<meta charset="utf-8">
<title>Hyperpigmentation Removal</title>
<link href="https://fonts.googleapis.com/css2?family=Montserrat:wght@300;400;600;700;800&family=Nothing+You+Could+Do&display=swap" rel="stylesheet">
<style>
  :root {
    --paper: #f3f3f3;
    --ink: #111111;
    --script-grey: #6b6b6b;
    --red-bright: #d81a2c;
    --red-deep: #6a0009;
    --photo-light: #ece9ea;
    --photo-skin: #e8c7b4;
    --photo-shadow: #b9b2b6;
    --leaf: #f2d9dc;
  }
  * { margin: 0; padding: 0; box-sizing: border-box; }
  html, body { width: 848px; height: 1200px; overflow: hidden; background: var(--paper); }
  .poster {
    position: relative;
    width: 848px;
    height: 1200px;
    background: linear-gradient(180deg, #f6f6f6 0%, var(--paper) 100%);
    font-family: "Montserrat", sans-serif;
    color: var(--ink);
    overflow: hidden;
  }
  .poster__photo { position: absolute; left: 0; top: 0; width: 848px; height: 1200px; }
  .poster__leaf {
    position: absolute; left: 0; top: 82px; width: 102px; height: 76px;
    background: var(--leaf);
    border-radius: 0 70% 10% 60%;
    transform: rotate(8deg);
  }
  .tagline { position: absolute; left: 0; top: 40px; width: 848px; height: 140px; }
  .brand {
    position: absolute; left: 686px; top: 232px;
    font-weight: 700; font-size: 38px; letter-spacing: 1px;
  }
  .tips {
    position: absolute; right: 30px; top: 614px;
    text-align: right;
  }
  .tips__title {
    font-weight: 600; font-size: 27px; line-height: 35px; letter-spacing: 0.5px;
    text-transform: uppercase;
  }
  .tips__list {
    list-style: none; margin-top: 35px;
    font-weight: 400; font-size: 26.5px; line-height: 35.5px; letter-spacing: 0.4px;
  }
  .headline { position: absolute; left: 0; top: 990px; width: 848px; height: 200px; }
</style>
</head>
<body>
<main class="poster">
  <svg class="poster__photo" viewBox="0 0 848 1200" role="img" aria-label="Photo of a woman relaxing on a treatment bed while a gloved practitioner uses a handheld skin device on her cheek">
    <defs>
      <linearGradient id="photoTone" x1="0" y1="0" x2="0.7" y2="1">
        <stop offset="0" stop-color="var(--photo-light)"/>
        <stop offset="0.45" stop-color="var(--photo-shadow)"/>
        <stop offset="0.7" stop-color="var(--photo-skin)"/>
        <stop offset="1" stop-color="#f1ebe8"/>
      </linearGradient>
    </defs>
    <path fill="url(#photoTone)" d="M100 160 L140 150 L190 175 L240 158 L300 170 L340 148 L380 170 L420 160 L460 195 L500 215 L540 235 L575 250 L610 275 L640 320 L655 355 L650 400 L690 470 L730 540 L745 610 L740 700 L730 800 L700 880 L640 930 L540 950 L420 960 L300 955 L200 965 L120 980 L40 980 L0 975 L0 300 L30 280 L40 240 L70 200 Z"/>
  </svg>
  <div class="poster__leaf" role="img" aria-label="Red line-art leaf ornament"></div>

  <svg class="tagline" viewBox="0 40 848 140" aria-label="Give your skin a little love">
    <text x="84" y="138" textLength="702" lengthAdjust="spacingAndGlyphs" fill="var(--script-grey)" font-family="'Nothing You Could Do', cursive" font-size="60">Give your skin a little love</text>
  </svg>
  <p class="brand">LOGO</p>

  <section class="tips">
    <h2 class="tips__title">Daily practices<br>to avoid<br>hyperpigmentation</h2>
    <ul class="tips__list">
      <li>Apply SPF regularly</li>
      <li>Avoid picking at pimples and blemishes</li>
      <li>Make a change in your diet</li>
      <li>Dont spray your perfume directly</li>
      <li>on skin Reduce the intake of alcohol</li>
    </ul>
  </section>

  <svg class="headline" viewBox="0 990 848 200" aria-label="Hyperpigmentation Removal">
    <defs>
      <linearGradient id="titleRed" x1="0" y1="0" x2="1" y2="0">
        <stop offset="0" stop-color="var(--red-bright)"/>
        <stop offset="0.35" stop-color="#c01526"/>
        <stop offset="1" stop-color="var(--red-deep)"/>
      </linearGradient>
    </defs>
    <text x="34" y="1053" textLength="797" lengthAdjust="spacingAndGlyphs" fill="url(#titleRed)" font-family="Montserrat, sans-serif" font-weight="800" font-size="66">HYPERPIGMENTATION</text>
    <text x="30" y="1176" textLength="798" lengthAdjust="spacingAndGlyphs" fill="url(#titleRed)" font-family="Montserrat, sans-serif" font-weight="300" font-size="153">REMOVAL</text>
  </svg>
</main>
</body>
</html>
```